Sell the dream! Property investment proposal document

We are looking for a proposal document which outlines our vision for property development. The purpose of the document is to raise investment from investors - sell the dream!
Brief summary:
Tarrow Dwellings Developments, is an emerging New Zealand property investment company with a focus on providing unique property investment opportunities.
Our expertise and capabilities in architectural modular homes provide us with a remarkable advantage in tackling the development of properties that are typically considered challenging, remote, or uniquely positioned.
Our specialization in this niche sector of property development not only sets us apart from competitors, but also paves the way for lucrative investment opportunities in the New Zealand property market.
Feel free to use any images from www.tarrowdwellings.co.nz
Target Market(s)
investors for a unique property development opportunity
Industry/Entity Type
luxury property development in unique locations throughout New Zealand
Font styles to use
Colors
Designer to choose only greyscale colors for use in the design.
Look and feel

```html
<!DOCTYPE html>
<html lang="en">
<head>
<meta charset="utf-8">
<title>Tarrow Dwellings Developments — Investment Proposal</title>
<link href="https://fonts.googleapis.com/css2?family=Montserrat:wght@300;400;600;700&family=Open+Sans:wght@400;600&display=swap" rel="stylesheet">
<style>
  :root{
    --canvas:#e4e4e4;
    --page:#2a2a2c;
    --page-alt:#262628;
    --ink:#f2f2f2;
    --muted:#a9a9ab;
    --accent:#9c8c5a;
    --rule:#4a4a4d;
    --photo-dark:#3c3f42;
    --photo-mid:#6f767a;
    --photo-light:#a9b0b3;
  }
  *{box-sizing:border-box;margin:0;padding:0}
  html,body{width:1200px;height:2312px;overflow:hidden;background:var(--canvas)}
  body{position:relative;font-family:"Open Sans",Arial,sans-serif;color:var(--ink)}
  .spread{position:absolute;left:35px;width:1130px;height:400px;display:flex;box-shadow:0 6px 18px rgba(0,0,0,.18)}
  .spread--cover{top:278px}
  .spread--overview{top:956px}
  .spread--advantage{top:1634px}
  .page{position:relative;width:565px;height:400px;background:var(--page);overflow:hidden}
  .page + .page{background:var(--page-alt);border-left:1px solid #1e1e20}
  .photo{position:absolute;background:linear-gradient(160deg,var(--photo-light) 0%,var(--photo-mid) 45%,var(--photo-dark) 100%)}
  .photo--green{background:linear-gradient(180deg,#b9c0c4 0%,#8e989c 40%,#55604a 75%,#3c4636 100%)}
  .photo--dusk{background:linear-gradient(180deg,#c9c2b2 0%,#8d8a83 45%,#4a4a48 100%)}
  .photo--framed{outline:2px solid var(--accent);outline-offset:4px}
  .page-footer{position:absolute;left:30px;bottom:18px;font:600 6.5px/1 "Montserrat",sans-serif;letter-spacing:2px;color:var(--muted);text-transform:uppercase}
  .page-number{position:absolute;right:24px;bottom:14px;width:14px;height:14px;border:1px solid var(--muted);border-radius:50%;font:600 6px/12px "Montserrat",sans-serif;text-align:center;color:var(--muted)}
  .heading{position:absolute;font:300 17px/1.1 "Montserrat",sans-serif;letter-spacing:1px;text-transform:uppercase;color:var(--ink)}
  .heading strong{font-weight:700;color:var(--accent)}
  .body-copy{position:absolute;font-size:7.5px;line-height:1.6;color:var(--muted)}
  .body-copy p + p{margin-top:7px}
  .wordmark{font:300 30px/1 "Montserrat",sans-serif;color:var(--ink);letter-spacing:.5px}
  .accent-bar{position:absolute;background:var(--accent)}
  /* cover back */
  .back-wordmark{position:absolute;left:40px;top:218px}
  .contact-list{position:absolute;left:40px;top:270px;display:grid;grid-template-columns:170px 170px;row-gap:8px;list-style:none;font-size:7.5px;color:var(--muted)}
  .contact-list li{display:flex;align-items:center;gap:6px}
  .contact-list svg{flex:none}
  .social{display:flex;gap:5px}
  .social span{width:9px;height:9px;border-radius:50%;background:var(--muted)}
  /* cover front */
  .cover-wordmark{position:absolute;left:36px;top:118px;font:300 52px/1 "Montserrat",sans-serif;color:var(--ink)}
  .cover-title{position:absolute;left:36px;top:190px;font:700 16px/1.15 "Montserrat",sans-serif;letter-spacing:1px;color:var(--ink)}
  .cover-title span{display:block;font-weight:300;color:var(--accent)}
  /* origins list */
  .origins{position:absolute;left:30px;top:70px;width:330px;list-style:none}
  .origins li{display:flex;gap:12px;align-items:flex-start;margin-bottom:22px}
  .origins .num{flex:none;width:16px;height:16px;border:1px solid var(--accent);font:600 7px/14px "Montserrat",sans-serif;text-align:center;color:var(--accent)}
  .origins p{font-size:7.5px;line-height:1.6;color:var(--muted)}
  .subhead{position:absolute;font:300 17px/1.15 "Montserrat",sans-serif;text-transform:uppercase;letter-spacing:1px}
  .subhead strong{display:block;font-weight:700}
</style>
</head>
<body>

<!-- Spread 1: back cover + front cover -->
<section class="spread spread--cover">
  <div class="page">
    <div class="photo photo--green" style="left:78px;top:84px;width:420px;height:100px" role="img" aria-label="Modular dark home set in a wide green rural landscape"></div>
    <div class="back-wordmark wordmark">Tarrow</div>
    <ul class="contact-list">
      <li><svg width="9" height="9" viewBox="0 0 10 10"><path d="M2 1h2l1 2-1.2 1A5 5 0 0 0 6 6.2L7 5l2 1v2c0 .6-.4 1-1 1A8 8 0 0 1 1 2c0-.6.4-1 1-1z" fill="#9c8c5a"/></svg>+64 21 555 0184</li>
      <li><svg width="9" height="9" viewBox="0 0 10 10"><circle cx="5" cy="5" r="4" fill="none" stroke="#9c8c5a"/><path d="M1 5h8M5 1c2 2 2 6 0 8M5 1c-2 2-2 6 0 8" fill="none" stroke="#9c8c5a" stroke-width=".7"/></svg>www.tarrowdwellings.co.nz</li>
      <li><svg width="9" height="9" viewBox="0 0 10 10"><rect x="1" y="2" width="8" height="6" fill="none" stroke="#9c8c5a"/><path d="M1 2l4 3 4-3" fill="none" stroke="#9c8c5a"/></svg>info@tarrowdwellings.co.nz</li>
      <li class="social"><span></span><span></span><span></span></li>
    </ul>
  </div>
  <div class="page">
    <div class="cover-wordmark">Tarrow</div>
    <h1 class="cover-title">DWELLINGS<span>DEVELOPMENTS</span></h1>
    <div class="body-copy" style="left:36px;top:240px;width:230px">
      <p>An investment proposal for architectural modular homes built in remote and uniquely positioned New Zealand locations.</p>
    </div>
    <div class="photo photo--green photo--framed" style="left:330px;top:70px;width:200px;height:130px" role="img" aria-label="Dark modular home among native trees"></div>
    <div class="photo" style="left:330px;top:218px;width:96px;height:70px" role="img" aria-label="Home exterior at dusk"></div>
    <div class="photo photo--green" style="left:434px;top:218px;width:96px;height:70px" role="img" aria-label="Home on a grassy hillside"></div>
    <div class="accent-bar" style="right:0;top:300px;width:4px;height:60px"></div>
    <div class="page-footer">www.tarrowdwellings.co.nz</div>
  </div>
</section>

<!-- Spread 2: business overview + origins -->
<section class="spread spread--overview">
  <div class="page">
    <h2 class="heading" style="left:30px;top:30px">Business <strong>Overview</strong></h2>
    <div class="body-copy" style="left:30px;top:70px;width:230px">
      <p>Tarrow Dwellings Developments is an emerging New Zealand property investment company offering unique opportunities in premium locations.</p>
      <p>Our expertise in architectural modular homes gives us a clear advantage on sites often seen as challenging, remote or uniquely positioned.</p>
      <p>Homes are crafted off site to exacting standards, then placed with care to respect the land and capture its views.</p>
      <p>This niche focus sets us apart from competitors and opens lucrative returns across the national property market.</p>
    </div>
    <div class="photo photo--green photo--framed" style="left:290px;top:70px;width:245px;height:250px" role="img" aria-label="Black modular home on a coastal hill with sea view"></div>
    <div class="page-footer">www.tarrowdwellings.co.nz</div>
    <div class="page-number">2</div>
  </div>
  <div class="page">
    <h2 class="heading" style="left:30px;top:30px">Business <strong>Origins</strong></h2>
    <ol class="origins">
      <li><span class="num">1</span><p>Founded by a small team of builders and designers with a shared passion for crafted, low impact homes.</p></li>
      <li><span class="num">2</span><p>Early projects proved that modular methods cut build time and cost on difficult remote sites.</p></li>
      <li><span class="num">3</span><p>A growing portfolio of coastal and rural homes earned strong demand from buyers and guests.</p></li>
      <li><span class="num">4</span><p>Today we invite investors to join the next stage of growth across New Zealand.</p></li>
    </ol>
    <div class="photo photo--dusk" style="left:400px;top:60px;width:135px;height:80px" role="img" aria-label="Home overlooking the sea"></div>
    <div class="photo" style="left:400px;top:150px;width:135px;height:80px" role="img" aria-label="Open plan living interior"></div>
    <div class="photo photo--green" style="left:400px;top:240px;width:135px;height:80px" role="img" aria-label="Deck framing a green valley view"></div>
    <div class="page-footer">www.tarrowdwellings.co.nz</div>
    <div class="page-number">3</div>
  </div>
</section>

<!-- Spread 3: competitive advantage + financial summary -->
<section class="spread spread--advantage">
  <div class="page">
    <div class="photo photo--dusk" style="left:0;top:0;width:240px;height:400px" role="img" aria-label="Modern home glowing at sunset by the water"></div>
    <div class="accent-bar" style="left:240px;top:60px;width:3px;height:60px"></div>
    <h2 class="subhead" style="left:270px;top:70px">Competitive<strong>Advantage</strong></h2>
    <div class="body-copy" style="left:270px;top:200px;width:250px">
      <p>Modular construction lets us build where others cannot, reducing risk and delays on remote land.</p>
      <p>Our design quality and site selection deliver homes that hold value and attract premium buyers.</p>
    </div>
    <div class="page-footer" style="left:270px">www.tarrowdwellings.co.nz</div>
    <div class="page-number">4</div>
  </div>
  <div class="page">
    <div class="body-copy" style="left:30px;top:30px;width:500px">
      <p>A summary of projected returns, development costs and capital requirements for the upcoming portfolio of homes.</p>
    </div>
    <h2 class="heading" style="left:30px;top:80px">Financial <strong>Summary</strong></h2>
    <div class="photo photo--dusk" style="left:30px;top:120px;width:160px;height:105px" role="img" aria-label="Home in tussock landscape"></div>
    <div class="photo photo--green" style="left:202px;top:120px;width:160px;height:105px" role="img" aria-label="Dark home above green fields"></div>
    <div class="photo" style="left:374px;top:120px;width:160px;height:105px" role="img" aria-label="Home on a ridge under cloudy sky"></div>
    <div class="body-copy" style="left:30px;top:245px;width:160px"><p>Target yield from short stay rental income is projected across all completed sites.</p></div>
    <div class="body-copy" style="left:202px;top:245px;width:160px"><p>Build costs are held low through repeatable modular design and factory efficiency.</p></div>
    <div class="body-copy" style="left:374px;top:245px;width:160px"><p>Capital growth is driven by rare locations and strong demand for design led homes.</p></div>
    <div class="page-footer">www.tarrowdwellings.co.nz</div>
    <div class="page-number">5</div>
  </div>
</section>

</body>
</html>
```